Website Online Research Solutions

We are a small European high-tech online research company.
With our own state of the art software we run online panels and are conducting reseach for companies. Partly research via our own panel and partly via panels we maintain for our customers.
Our current website is old and outdatet: www.pravelo.nl.
We are in the process to change the content of the site. We want a modern, european and businesslike design for our new website.
Our logo has to stay the same (left uppersite of our website and attached) but can be changed a little to adapt it to the new design of the website. The colors of the site are up to you.
Target Market(s)
Marketeers and researchers of large and middle size companies in all kind of fields.
Industry/Entity Type
Online
Look and feel
Each slider illustrates characteristics of the customer's brand and the style your logo design should communicate.

```html
<!DOCTYPE html>
<html lang="nl">
<head>
<meta charset="utf-8">
<title>Pravelo – Online gegevensverzameling</title>
<link href="https://fonts.googleapis.com/css2?family=Open+Sans:wght@400;600&display=swap" rel="stylesheet">
<style>
  :root {
    --stage: #2a2420;
    --page-top: #262626;
    --page-bottom: #121212;
    --ink: #ffffff;
    --text: #a3a3a3;
    --text-dim: #7a7a7a;
    --accent: #2aa3d6;
    --accent-tab: #1f9cc4;
    --band: #e9ecef;
    --band-text: #333a40;
    --footer: #0d0d0d;
    --rule: #333333;
  }
  * { margin: 0; padding: 0; box-sizing: border-box; }
  html, body { width: 1200px; height: 900px; overflow: hidden; }
  body {
    background: var(--stage);
    font-family: "Open Sans", Arial, sans-serif;
    position: relative;
  }
  .site {
    position: absolute; left: 270px; top: 10px;
    width: 660px; height: 880px;
    background: linear-gradient(180deg, var(--page-top), var(--page-bottom) 75%);
    box-shadow: 0 6px 24px rgba(0,0,0,.6);
    overflow: hidden;
  }
  /* header */
  .site-header { position: absolute; left: 0; top: 0; width: 660px; height: 110px; z-index: 3; }
  .brand {
    position: absolute; left: 40px; top: 38px;
    display: flex; align-items: center; gap: 8px;
    color: var(--ink); font-size: 19px; font-weight: 600; letter-spacing: .3px;
    line-height: 26px;
  }
  .brand-mark { width: 14px; height: 14px; background: var(--ink); }
  .main-nav {
    position: absolute; right: 26px; top: 38px;
    display: flex; gap: 6px; list-style: none;
  }
  .main-nav > li { position: relative; }
  .main-nav a {
    display: block; color: var(--ink); text-decoration: none;
    font-size: 11px; line-height: 14px; padding: 6px 4px;
  }
  .main-nav > li.active > a { background: var(--accent-tab); padding: 6px 7px; }
  .submenu {
    position: absolute; left: 0; top: 100%; width: 80px;
    background: var(--accent-tab); padding: 6px 6px 8px;
    list-style: none;
  }
  .submenu li { color: var(--ink); font-size: 8px; line-height: 11px; white-space: nowrap; }
  /* hero */
  .hero { position: absolute; left: 40px; top: 118px; width: 580px; height: 230px; }
  .hero-photo {
    position: absolute; left: 0; top: 0; width: 580px; height: 185px;
    background: linear-gradient(100deg, #f4f6f8 0%, #c9d9ea 45%, #4d78a8 80%, #1e3550 100%);
  }
  .hero-pie { position: absolute; left: -14px; top: 118px; width: 92px; height: 80px; z-index: 2; }
  .hero-caption {
    position: absolute; left: 70px; top: 185px; width: 510px; height: 44px;
    background: var(--band); color: var(--band-text);
    font-size: 12px; line-height: 16px; padding: 6px 12px 0 40px;
  }
  .hero-caption em { color: var(--accent); font-style: normal; }
  /* content */
  .content { position: absolute; left: 58px; top: 400px; width: 560px; display: flex; gap: 40px; }
  .column { width: 250px; }
  .column h2 { color: var(--accent); font-size: 13px; font-weight: 600; margin-bottom: 8px; }
  .column p { color: var(--text); font-size: 8.5px; line-height: 12px; margin-bottom: 10px; }
  .column-photo { width: 175px; height: 88px; margin: 6px 0 14px; }
  .photo-left { background: linear-gradient(135deg, #eef1f4, #b9c6d2 60%, #6f8296); }
  .photo-right { width: 230px; height: 105px; background: linear-gradient(120deg, #f1f1f1, #cfd6dc 55%, #8fa2b3); }
  /* footer */
  .site-footer {
    position: absolute; left: 0; top: 750px; width: 660px; height: 130px;
    background: var(--footer); border-top: 1px solid var(--rule);
    display: flex; gap: 30px; padding: 14px 40px 0 58px;
  }
  .footer-col { font-size: 7.5px; line-height: 11px; color: var(--text-dim); list-style: none; }
  .footer-col .lead { color: var(--accent); }
  .footer-col.news { width: 140px; }
</style>
</head>
<body>
  <div class="site">
    <header class="site-header">
      <div class="brand"><span class="brand-mark"></span>Pravelo</div>
      <ul class="main-nav">
        <li><a href="#">Algemeen</a></li>
        <li class="active"><a href="#">Producten</a>
          <ul class="submenu">
            <li>Dataverzameling</li>
            <li>Analyse</li>
            <li>Klanten</li>
            <li>Dataopslag</li>
            <li>Panel, kosten</li>
          </ul>
        </li>
        <li><a href="#">Demo´s</a></li>
        <li><a href="#">Media</a></li>
        <li><a href="#">Referenties</a></li>
        <li><a href="#">Personeel</a></li>
        <li><a href="#">Contact</a></li>
      </ul>
    </header>

    <section class="hero">
      <div class="hero-photo" role="img" aria-label="Foto van een beeldscherm met blauwe beursgrafieken"></div>
      <svg class="hero-pie" viewBox="0 0 92 80" aria-hidden="true">
        <ellipse cx="46" cy="48" rx="40" ry="22" fill="#8a5a14"/>
        <path d="M46 40 L46 18 A40 22 0 0 1 86 40 Z" fill="#e8b630"/>
        <path d="M46 40 L86 40 A40 22 0 0 1 30 61 Z" fill="#3f8fd0"/>
        <path d="M46 40 L30 61 A40 22 0 0 1 6 40 Z" fill="#d9452e"/>
        <path d="M46 40 L6 40 A40 22 0 0 1 46 18 Z" fill="#7cbd3a"/>
      </svg>
      <p class="hero-caption">Pravelo is gespecialiseerd in <em>online gegevensverzameling</em> en analyse en is werkzaam voor internationale opdrachtgevers.</p>
    </section>

    <main class="content">
      <article class="column">
        <h2>Dataverzameling</h2>
        <p>Vragenlijsten die door Pravelo worden geprogrammeerd zijn dynamisch gegenereerde vragenlijsten die in de "look &amp; feel" worden geprogrammeerd van onze klanten en/of de produkten van onze klanten.</p>
        <div class="column-photo photo-left" role="img" aria-label="Illustratie van een groep mensen rond een wereldkaart"></div>
        <p>Pravelo programmeert vragenlijsten voor gegevensverzameling via internet, telefoon of via e-mail. Recentelijk hebben we zelfs een betrouwbare methode ontwikkeld voor onderzoek via sms.</p>
        <p>De vele honderden onderzoeken die wij hebben geprogrammeerd variëren van eenvoudige onderzoeken zoals quickpolls met een aantal korte stellingen tot complexe conjoint studies, tracking onderzoek en usability tests.</p>
      </article>
      <article class="column">
        <h2>Streaming audio/video</h2>
        <p>Daarnaast hebben wij een nieuwe techniek ontwikkeld voor online onderzoek met behulp van pre-testing van radio- en tv-commercials waarbij gebruik gemaakt wordt van streaming audio/video.</p>
        <p>Pravelo stelt haar opdrachtgevers in staat om op eenvoudige wijze de verschillende onderdelen van een commercial online te bekijken en direct online te analyseren via een online analysetool. Hierdoor is deze analyse sneller en goedkoper dan wanneer dit via een traditionele methode gebeurt. Ook kunnen bedrijven hun eigen respondenten gebruiken.</p>
        <div class="column-photo photo-right" role="img" aria-label="Foto van een beeldscherm met een online vragenlijst en woorden als opinie en antwoord"></div>
      </article>
    </main>

    <footer class="site-footer">
      <ul class="footer-col">
        <li class="lead">» Algemeen</li>
        <li class="lead">» Producten</li>
        <li>Dataverzameling</li>
        <li>Analyse</li>
        <li>Klanten</li>
        <li>Dataopslag</li>
        <li>Panel, kosten</li>
      </ul>
      <ul class="footer-col">
        <li class="lead">» Demo's</li>
        <li class="lead">» Media</li>
        <li class="lead">» Referenties</li>
        <li class="lead">» Personeel</li>
      </ul>
      <ul class="footer-col news">
        <li class="lead">Nieuws</li>
        <li>Nieuw panel gestart voor een grote klant in de zorgsector. Meer dan duizend leden doen nu wekelijks mee aan onderzoek en rapportage.</li>
      </ul>
      <ul class="footer-col">
        <li>Pravelo BV</li>
        <li>Kanaalweg 12</li>
        <li>5701 AB Helmond</li>
        <li>T 0492 123456</li>
        <li>F 0492 123457</li>
        <li>E info@pravelo.nl</li>
        <li>www.pravelo.nl</li>
      </ul>
    </footer>
  </div>
</body>
</html>
```